Wedding Marloes & Joost - Save the Date Wedding Card

I would like to have a creative save the date wedding card. We like grey/black/white colors and modern/ plain and simple.
I like the Save the Date copy big and book a flight copy smaller. I like stylish fonts for the save the date copy
Copy front:
Save the Date & book a flight
7-10-2017 Denia (Spanje)
Marloes & Joost
Onze dag is niet compleet zonder jou!
Copy back:
6-10 preferred travel date
7-10 wedding ceremony/drinks/dinner/party
8-10 hangover breakfast
Nearest Airports Valencia & Alicante
More info will be available soon!
Target Market(s)
wedding guests
Industry/Entity Type
Wedding

```html
<!DOCTYPE html>
<html lang="nl">
<head>
<meta charset="utf-8">
<title>Save the Date – Marloes &amp; Joost</title>
<link rel="stylesheet" href="https://fonts.googleapis.com/css2?family=Great+Vibes&family=Bitter:wght@300;400;700&display=swap">
<style>
  :root {
    --card-black: #000000;
    --panel-white: #ffffff;
    --lace-white: #f2f2f2;
    --ink: #3a3a3a;
    --ornament-tone: #2b2b2b;
    --ornament-soft: #3d3d3d;
    --divider-grey: #9a9a9a;
  }
  html, body {
    margin: 0;
    padding: 0;
    width: 1200px;
    height: 858px;
    overflow: hidden;
    background: var(--card-black);
  }
  .save-the-date-card {
    position: relative;
    width: 1200px;
    height: 858px;
    background: var(--card-black);
  }
  .card-art {
    position: absolute;
    inset: 0;
    display: block;
  }
  .swirl-ornament { fill: url(#swirlTone); }
  .lace-border { fill: var(--lace-white); }
  .center-panel { fill: var(--panel-white); }
  .headline-script {
    font-family: "Great Vibes", cursive;
    fill: var(--ink);
  }
  .headline-main { font-size: 112px; }
  .headline-amp { font-size: 150px; }
  .subline {
    font-family: "Bitter", serif;
    font-weight: 300;
    font-size: 58px;
    fill: var(--ink);
  }
  .divider-ornament { fill: var(--divider-grey); }
  .divider-line { stroke: var(--ink); stroke-width: 2; }
  .couple-names {
    font-family: "Bitter", serif;
    font-weight: 700;
    font-size: 35px;
    fill: var(--ink);
  }
  .event-details {
    font-family: "Bitter", serif;
    font-weight: 300;
    font-size: 29px;
    fill: var(--ink);
  }
  .tagline {
    font-family: "Bitter", serif;
    font-weight: 300;
    font-size: 23px;
    fill: var(--ink);
  }
</style>
</head>
<body>
<main class="save-the-date-card">
  <svg class="card-art" viewBox="0 0 1200 858" width="1200" height="858" xmlns="http://www.w3.org/2000/svg">
    <defs>
      <linearGradient id="swirlTone" x1="0" y1="0" x2="0" y2="1">
        <stop offset="0" stop-color="#2b2b2b"/>
        <stop offset="1" stop-color="#3d3d3d"/>
      </linearGradient>
      <path id="headlineArc" d="M 320 330 Q 600 40 880 335"/>
    </defs>

    <!-- side flourishes -->
    <g class="side-flourishes">
      <rect class="swirl-ornament" x="32" y="26" width="172" height="380" rx="60" role="img" aria-label="White curling swirl flourish, upper left"/>
      <rect class="swirl-ornament" x="32" y="450" width="172" height="385" rx="60" role="img" aria-label="White curling swirl flourish, lower left"/>
      <rect class="swirl-ornament" x="1000" y="26" width="172" height="380" rx="60" role="img" aria-label="White curling swirl flourish, upper right"/>
      <rect class="swirl-ornament" x="1000" y="450" width="172" height="385" rx="60" role="img" aria-label="White curling swirl flourish, lower right"/>
    </g>

    <!-- doily frame -->
    <circle class="lace-border" cx="605" cy="430" r="412" role="img" aria-label="Round white lace doily border"/>
    <circle class="center-panel" cx="605" cy="430" r="352"/>

    <!-- headline -->
    <text class="headline-script headline-main">
      <textPath href="#headlineArc" startOffset="50%" text-anchor="middle">Save the Date</textPath>
    </text>
    <text class="headline-script headline-amp" x="598" y="362" text-anchor="middle">&amp;</text>

    <text class="subline" x="605" y="455" text-anchor="middle">Book a Flight</text>

    <!-- divider -->
    <rect class="divider-ornament" x="506" y="484" width="196" height="30" rx="15" role="img" aria-label="Small scrollwork ornament"/>
    <line class="divider-line" x1="396" y1="521" x2="813" y2="521"/>

    <!-- details -->
    <text class="couple-names" x="605" y="570" text-anchor="middle">Marloes &amp; Joost</text>
    <text class="event-details" x="600" y="616" text-anchor="middle">7 oktober 2017</text>
    <text class="event-details" x="605" y="652" text-anchor="middle">Denia, Spanje</text>
    <text class="tagline" x="605" y="700" text-anchor="middle">Onze dag is niet compleet</text>
    <text class="tagline" x="605" y="730" text-anchor="middle">zonder jou!</text>
  </svg>
</main>
</body>
</html>
```